Larkspur Advisory Biz Card Template
Corp Biz Card
Professional
Desmond Hallowell
Managing Director
desmond@larkspuradvisory-example.com
www.larkspuradvisory-example.com
Card must have bleed areas set, and sized as per the attached PDF guides.
Card should be editable for each person in company.
Our Mission:
"To assist our clients in achieving their business objectives through the successful implementation of true leading edge technology"
Services for:
* KTV Nimbus Inventory and Linkage Charting - NILC
* KTV ScriptForge - KTSF
* KTV WatchGrid
* KTV Ticket Hub Rapid
* Project Management
* Project Resourcing

```html
<!DOCTYPE html>
<html lang="en">
<head>
<meta charset="utf-8">
<title>Larkspur Advisory – Business Card</title>
<link rel="stylesheet" href="https://fonts.googleapis.com/css2?family=Source+Sans+3:ital,wght@0,400;0,600;0,700;1,600&display=swap">
<style>
  :root {
    --backdrop: #e8e5e1;
    --card-white: #ffffff;
    --brand-blue: #27a3d3;
    --brand-orange: #e0701e;
    --ink-dark: #2b2b2b;
    --ink-light: #ffffff;
  }
  * { box-sizing: border-box; margin: 0; padding: 0; }
  html, body {
    width: 1200px; height: 780px; overflow: hidden;
    background: var(--backdrop);
    font-family: "Source Sans 3", "Myriad Pro", Arial, sans-serif;
  }
  .business-card {
    position: absolute; left: 110px; top: 100px;
    width: 980px; height: 580px;
    border-radius: 30px; overflow: hidden;
    background: var(--card-white);
    box-shadow: 0 6px 22px rgba(0,0,0,0.18);
  }
  .card-front { position: absolute; inset: 0 0 auto 0; height: 322px; }
  .brand-lockup {
    position: absolute; left: 240px; top: 112px;
    display: flex; align-items: center; gap: 22px;
  }
  .brand-mark {
    width: 62px; height: 62px; background: var(--brand-orange);
  }
  .brand-name {
    font-size: 78px; font-weight: 700; letter-spacing: -1px;
    color: var(--ink-dark); line-height: 1;
  }
  .accent-rule {
    position: absolute; left: 0; right: 0; top: 322px; height: 5px;
    background: var(--brand-orange);
  }
  .contact-band {
    position: absolute; left: 0; right: 0; top: 327px; bottom: 0;
    background: var(--brand-blue); color: var(--ink-light);
  }
  .person {
    position: absolute; right: 520px; top: 94px; text-align: right;
  }
  .person-name { font-size: 27px; font-weight: 700; line-height: 1.2; }
  .person-role { font-size: 20px; font-weight: 600; font-style: italic; line-height: 1.3; }
  .band-divider {
    position: absolute; left: 484px; top: 42px; width: 2px; height: 176px;
    background: var(--ink-light);
  }
  .contact-list {
    position: absolute; left: 506px; top: 40px; list-style: none;
  }
  .contact-list li {
    display: flex; align-items: center; gap: 12px;
    font-size: 19px; line-height: 35px; white-space: nowrap;
  }
  .contact-icon { width: 20px; height: 20px; flex: none; }
</style>
</head>
<body>
  <div class="business-card">
    <div class="card-front">
      <div class="brand-lockup">
        <div class="brand-mark"></div>
        <div class="brand-name">Larkspur Advisory</div>
      </div>
    </div>
    <div class="accent-rule"></div>
    <div class="contact-band">
      <div class="person">
        <p class="person-name">Desmond Hallowell</p>
        <p class="person-role">Managing Director</p>
      </div>
      <div class="band-divider"></div>
      <ul class="contact-list">
        <li>
          <svg class="contact-icon" viewBox="0 0 20 20" aria-hidden="true"><path d="M5 2c1 0 2 3 2 4s-1.5 1.5-1 2.5 2.5 4 4 4.5 1.5-1 2.5-1 4 1 4 2-1.5 3-3.5 3C7 17 3 10 3 5c0-2 1-3 2-3z" fill="#fff"/></svg>
          <span>0800 555 0142</span>
        </li>
        <li>
          <svg class="contact-icon" viewBox="0 0 20 20" aria-hidden="true"><rect x="6" y="1" width="8" height="18" rx="1.5" fill="#fff"/><rect x="7.5" y="3" width="5" height="6" fill="#27a3d3"/></svg>
          <span>07700 900 318</span>
        </li>
        <li>
          <svg class="contact-icon" viewBox="0 0 20 20" aria-hidden="true"><rect x="5" y="2" width="10" height="6" fill="#fff"/><rect x="2" y="8" width="16" height="8" rx="1" fill="#fff"/><rect x="5" y="13" width="10" height="5" fill="#fff" stroke="#27a3d3" stroke-width="1"/></svg>
          <span>0800 555 0143</span>
        </li>
        <li>
          <svg class="contact-icon" viewBox="0 0 20 20" aria-hidden="true"><text x="10" y="16" text-anchor="middle" font-size="18" font-weight="700" fill="#fff" font-family="Arial, sans-serif">@</text></svg>
          <span>desmond@larkspuradvisory-example.com</span>
        </li>
        <li>
          <svg class="contact-icon" viewBox="0 0 20 20" aria-hidden="true"><g fill="none" stroke="#fff" stroke-width="1.6"><circle cx="10" cy="10" r="8"/><ellipse cx="10" cy="10" rx="3.5" ry="8"/><path d="M2 10h16"/></g></svg>
          <span>www.larkspuradvisory-example.com</span>
        </li>
      </ul>
    </div>
  </div>
</body>
</html>
```